7 3/4 x 5 1/4 Annual Banquet Invitation

Design an invitation for our Chamber's annual banquet. It will be a single sided invitation 5 1/4" wide by 7 3/4" height that we will print in-house. Our logo is attached. The theme is "Serving Together". I was thinking of an image with two hands coming together in a handshake, perhaps intertwining our logo colors. This is just a thought. I am open for any suggestions! Text for the invitation should be as follows: The Board of Directors and Staff cordially invites you to attend the 64th Yearly Gathering & Micro-Trade Fair - Monday, January 22, 2018. 5:30 p.m. Social, 6:00 p.m. Dinner. Cedarvale Chapel, 4819 Harlan P. Moss Rd S, Brackenford. Please RSVP by January 18, 2018.

Target Market(s)

This invitation will be printed and mailed to our membership.

Industry/Entity Type

Business Management

Colors
33a6d7
faa54b
0355a3
00a990

Requirements
Must have
• Event info as indentified above.
Nice to have
• Our Logo

```html
<!DOCTYPE html>
<html lang="en">
<head>
<meta charset="utf-8">
<title>64th Annual Banquet Invitation</title>
<link rel="stylesheet" href="https://fonts.googleapis.com/css2?family=Arimo:wght@700&family=Pacifico&family=Roboto+Slab:wght@300&family=Sorts+Mill+Goudy&display=swap">
<style>
  :root {
    --backdrop: #0453a2;
    --paper: #fdfbf4;
    --ink: #0355a3;
    --diamond: #ffffff;
    --bloom-purple: #7a3b7e;
    --bloom-magenta: #b8326f;
    --bloom-red: #d9334a;
    --bloom-orange: #ef7a45;
    --bloom-gold: #f2c15a;
    --bloom-teal: #4fb9c4;
    --mark-ring: #33a6d7;
  }
  * { margin: 0; padding: 0; box-sizing: border-box; }
  html, body { width: 1200px; height: 1200px; overflow: hidden; background: var(--backdrop); }
  .canvas { position: relative; width: 1200px; height: 1200px; background: var(--backdrop); }
  .invitation {
    position: absolute; left: 194px; top: 0; width: 812px; height: 1200px;
    background: var(--paper); overflow: hidden;
    box-shadow: 0 0 24px rgba(0,0,0,.25);
  }
  .bloom-art {
    position: absolute; left: 0; top: 0; width: 400px; height: 735px;
    clip-path: polygon(0 13%, 18% 0, 95% 0, 100% 20%, 92% 37%, 100% 62%, 88% 70%, 72% 84%, 30% 100%, 8% 95%, 0 88%);
    background:
      radial-gradient(circle at 62% 14%, var(--bloom-purple) 0, transparent 38%),
      radial-gradient(circle at 90% 45%, var(--bloom-teal) 0, transparent 30%),
      radial-gradient(circle at 82% 68%, var(--bloom-gold) 0, transparent 30%),
      radial-gradient(circle at 10% 80%, var(--bloom-magenta) 0, transparent 40%),
      radial-gradient(circle at 45% 88%, var(--bloom-red) 0, transparent 40%),
      linear-gradient(165deg, var(--bloom-orange), var(--bloom-red) 55%, var(--bloom-orange));
  }
  .anniversary-diamond {
    position: absolute; left: 8px; top: 150px; width: 272px; height: 272px;
    background: var(--diamond); transform: rotate(45deg);
    box-shadow: 8px 8px 20px rgba(0,0,0,.2);
  }
  .anniversary-number {
    position: absolute; left: 70px; top: 218px;
    font-family: "Arimo", sans-serif; font-weight: 700; font-size: 145px;
    line-height: 1; color: var(--ink); letter-spacing: -3px;
  }
  .anniversary-number sup {
    font-size: 34px; vertical-align: top; position: relative; top: 18px; left: 4px; letter-spacing: 0;
  }
  .event-title {
    position: absolute; left: 400px; top: 160px;
    font-family: "Pacifico", cursive; font-weight: 400; font-size: 96px; line-height: 112px;
    color: var(--ink);
  }
  .event-kind {
    position: absolute; left: 402px; top: 420px;
    font-family: "Roboto Slab", serif; font-weight: 300; font-size: 42px;
    letter-spacing: 17.5px; color: var(--ink);
  }
  .body-text {
    position: absolute; left: 400px;
    font-family: "Sorts Mill Goudy", serif; font-size: 23px; line-height: 33px;
    color: var(--ink);
  }
  .invite-message { top: 500px; left: 404px; }
  .invite-message .lead { padding-left: 9px; }
  .event-when { top: 740px; }
  .event-where { top: 930px; }
  .rsvp { top: 1102px; }
  .divider { position: absolute; left: 404px; width: 332px; height: 20px; }
  .divider-1 { top: 667px; }
  .divider-2 { top: 857px; }
  .divider-3 { top: 1045px; left: 400px; }
  .host {
    position: absolute; left: 56px; top: 940px; width: 300px; text-align: center;
  }
  .host-mark {
    width: 130px; height: 130px; border-radius: 50%;
    border: 5px solid var(--mark-ring); margin: 0 auto 22px;
  }
  .host-name {
    font-family: "Arimo", sans-serif; font-weight: 700; color: var(--ink);
    text-transform: uppercase; line-height: 1;
  }
  .host-name .line-main { display: block; font-size: 23px; letter-spacing: -.2px; }
  .host-name .line-sub { display: block; font-size: 13px; letter-spacing: 3.2px; margin-top: 3px; }
</style>
</head>
<body>
<div class="canvas">
  <article class="invitation">
    <div class="bloom-art" role="img" aria-label="Burst of colourful overlapping petals in purple, red, orange, gold and teal"></div>
    <div class="anniversary-diamond"></div>
    <div class="anniversary-number">64<sup>th</sup></div>

    <h1 class="event-title">Annual<br>Banquet</h1>
    <p class="event-kind">invitation</p>

    <p class="body-text invite-message"><span class="lead">The Board of Directors and Staff</span><br>cordially invites you to attend<br>the 64th Yearly Gathering &amp;<br>Micro-Trade Fair</p>

    <svg class="divider divider-1" viewBox="0 0 332 20" aria-hidden="true">
      <path d="M10 1 L19 10 L10 19 L1 10Z M322 1 L331 10 L322 19 L313 10Z" fill="#0355a3"/>
      <circle cx="29" cy="10" r="3.5" fill="#0355a3"/><circle cx="303" cy="10" r="3.5" fill="#0355a3"/>
      <line x1="29" y1="10" x2="303" y2="10" stroke="#0355a3" stroke-width="1.5"/>
    </svg>

    <p class="body-text event-when">Monday - January 22, 2018.<br>5:30 p.m. Social<br>6:00 p.m. Dinner.</p>

    <svg class="divider divider-2" viewBox="0 0 332 20" aria-hidden="true">
      <path d="M10 1 L19 10 L10 19 L1 10Z M322 1 L331 10 L322 19 L313 10Z" fill="#0355a3"/>
      <circle cx="29" cy="10" r="3.5" fill="#0355a3"/><circle cx="303" cy="10" r="3.5" fill="#0355a3"/>
      <line x1="29" y1="10" x2="303" y2="10" stroke="#0355a3" stroke-width="1.5"/>
    </svg>

    <p class="body-text event-where">Cedarvale Chapel,<br>4819 Harlan P. Moss Rd S,<br>Brackenford.</p>

    <svg class="divider divider-3" viewBox="0 0 332 20" aria-hidden="true">
      <path d="M10 1 L19 10 L10 19 L1 10Z M322 1 L331 10 L322 19 L313 10Z" fill="#0355a3"/>
      <circle cx="29" cy="10" r="3.5" fill="#0355a3"/><circle cx="303" cy="10" r="3.5" fill="#0355a3"/>
      <line x1="29" y1="10" x2="303" y2="10" stroke="#0355a3" stroke-width="1.5"/>
    </svg>

    <p class="body-text rsvp">Please RSVP by January 18, 2018.</p>

    <div class="host">
      <div class="host-mark"></div>
      <p class="host-name"><span class="line-main">Harborline Chamber</span><span class="line-sub">of Commerce &amp; Tourism</span></p>
    </div>
  </article>
</div>
</body>
</html>
```